Fashion Brand Store Openning
Rollups, flyers, and large sticker
Thank you for participating.
We have chose several of those great desings to use in our grand openning. We would like to invite you in our next project also, which will be a small magazine, will be posted soon.
Milena, for design # 4 would you please place our website in the bottom and "Now Open", to have the final design
Honeslty, I don't have a particular size in mind.
for the flyers, it will be A4 size.
Roll ups and stickers, nothing really particular.
Hello. Have you mentioned anywhere a size? If not, can you provide any, i'm sure it will help us, designers.
design # 14 and 13. they are decent, but need more illistrative work to become luxury and fancy.
Milena really your work is great. Please, avoid using this large and casual font for "now Open." I would like to see more simpler and clear font for this statment.
I am extending the time for 5 more days
Great works Milena. Design #4. But, what is this website in the design? is it your? We prefer to put ours, if you don't mind: www.varletoncasa.co.uk
Korvaet: I like your design and the combinations of color used in the design, the grey, gold, and black.
You can use text like: "Now Open," "The Original Designs of Marco Teslavardi."
I will be waiting to see more of your good work
Hi tumerosk,
Can we get some text, which will be on the material, please?
Regards,
Milenka
Here you go I uploaded number of diffrent desings. Please, do not use all of them. One or two images is enough.
where the images ,...???? please check again ..i think i am interesting, can u upload again..? or if u dont mind i will use stock photo "p lumo" but it must u purchase. if u upload soon maybe one or two hours from here i will making for you soon. :)
warm regards
Please, check the images I upload it contains number of diffrent designs we made earlier.
Also, pay attention to the images of dresses it can be used in the flyers and roll ups, all these dresses are the Original Designs of Marco Teslavardi.

```html
<!DOCTYPE html>
<html lang="en">
<head>
<meta charset="utf-8">
<title>Marco Teslavardi – Now Open</title>
<link href="https://fonts.googleapis.com/css2?family=Cinzel:wght@400;500&family=Cormorant+Garamond:ital,wght@0,500;1,500&display=swap" rel="stylesheet">
<style>
  :root {
    --paper: #ffffff;
    --gold: #c9a43a;
    --gold-light: #e2c46a;
    --black: #0c0c0c;
    --charcoal: #2a2a2a;
    --grey-light: #d8d8d8;
    --grey-mid: #8f8f8f;
  }
  * { margin: 0; padding: 0; box-sizing: border-box; }
  html, body {
    width: 1200px; height: 1075px; overflow: hidden;
    background: var(--paper);
  }
  .canvas { position: relative; width: 1200px; height: 1075px; }

  .rollup, .banner { position: absolute; overflow: hidden; }

  /* Roll-up */
  .rollup {
    left: 23px; top: 14px; width: 542px; height: 1026px;
    background: radial-gradient(ellipse at 50% 40%, var(--grey-light) 0%, #b5b5b5 45%, var(--grey-mid) 100%);
  }
  .rollup .photo {
    position: absolute; left: 110px; top: 0; width: 300px; height: 975px;
    background:
      linear-gradient(180deg, rgba(60,60,60,0.55) 0%, rgba(60,60,60,0.25) 30%, transparent 32%),
      linear-gradient(180deg, transparent 30%, #b0503a 36%, #3f7fa0 44%, #c99a2e 52%, #7a3f86 60%, transparent 64%),
      linear-gradient(180deg, transparent 62%, rgba(40,40,40,0.45) 66%, rgba(30,30,30,0.6) 95%);
    opacity: 0.85;
    border-radius: 140px 140px 20px 20px;
  }

  .now-open {
    position: absolute; font-family: "Cinzel", serif; font-weight: 400;
    color: var(--gold); white-space: nowrap;
  }
  .rollup .now-open { left: 0; width: 100%; top: 392px; text-align: center; font-size: 44px; letter-spacing: 26px; text-indent: 26px; }

  .brand {
    position: absolute; display: flex; flex-direction: column; align-items: center;
    font-family: "Cormorant Garamond", serif; font-weight: 500; color: var(--gold);
    text-align: center; line-height: 1.05;
  }
  .brand .seal { border: 2px solid var(--gold); border-radius: 50%; }
  .rollup .brand { left: 0; width: 100%; top: 725px; font-size: 28px; }
  .rollup .brand .seal { width: 62px; height: 62px; margin-bottom: 10px; }

  .tagline {
    position: absolute; font-family: "Cinzel", serif; color: var(--gold);
    white-space: nowrap; letter-spacing: 1px;
  }
  .tagline em { font-family: "Cormorant Garamond", serif; font-style: italic; text-transform: none; }
  .rollup .tagline { left: 0; width: 100%; top: 898px; text-align: center; font-size: 18px; }

  .footer-bar {
    position: absolute; left: 0; right: 0; bottom: 0;
    background: var(--black); border-top: 3px solid var(--gold);
    display: flex; align-items: center; justify-content: center;
  }
  .website { font-family: "Cinzel", serif; color: var(--gold-light); letter-spacing: 1px; }
  .rollup .footer-bar { height: 52px; }
  .rollup .website { font-size: 15px; }

  /* Landscape banner */
  .banner {
    left: 597px; top: 281px; width: 556px; height: 488px;
    background: linear-gradient(180deg, #3a3a3a 0%, var(--charcoal) 35%, var(--black) 100%);
  }
  .banner .photo {
    position: absolute; right: 0; top: 0; width: 220px; height: 428px;
    background:
      linear-gradient(90deg, rgba(0,0,0,0) 0%, rgba(150,150,150,0.35) 40%, rgba(190,190,190,0.45) 100%),
      linear-gradient(180deg, rgba(120,120,120,0.5) 0%, transparent 30%, #a04a38 38%, #3c7898 50%, #c0932c 62%, #6f3b7d 74%, rgba(60,60,60,0.6) 90%);
  }
  .banner .tagline { left: 20px; top: 66px; font-size: 18px; }
  .banner .brand { left: 95px; width: 150px; top: 180px; font-size: 24px; }
  .banner .brand .seal { width: 56px; height: 56px; margin-bottom: 8px; }
  .banner .now-open { left: 228px; top: 250px; font-size: 27px; letter-spacing: 9px; }
  .banner .footer-bar { height: 58px; }
  .banner .website { font-size: 15px; }
</style>
</head>
<body>
<div class="canvas">

  <section class="rollup">
    <div class="photo" role="img" aria-label="Black and white photo of a model in a multicoloured tiered dress, standing with one hand on hip"></div>
    <h1 class="now-open">NOW OPEN</h1>
    <div class="brand"><span class="seal"></span>Marco<br>Teslavardi</div>
    <p class="tagline">THE ORIGINAL DESIGNS <em>of</em> MARCO TESLAVARDI</p>
    <div class="footer-bar"><span class="website">WWW.VARLETONCASA.CO.UK</span></div>
  </section>

  <section class="banner">
    <div class="photo" role="img" aria-label="Cropped black and white photo of a model wearing a multicoloured tiered dress"></div>
    <p class="tagline">THE ORIGINAL DESIGNS <em>of</em> MARCO TESLAVARDI</p>
    <div class="brand"><span class="seal"></span>Marco<br>Teslavardi</div>
    <h2 class="now-open">NOW OPEN</h2>
    <div class="footer-bar"><span class="website">WWW.VARLETONCASA.CO.UK</span></div>
  </section>

</div>
</body>
</html>
```